Values and Organizational Purpose Signage

We recently solidified our company values, organizatioanal purpose and strategic vision. I'd like to develop some tasteful (not overly corporate) signage of these values to display in our office.

I've attached the hand-written values and purpose that my core team members then initialed acknowleding they align along with the signage at the front of our office to provide some perspective on our brand identity.

Industry/Entity Type

It Company

Font styles to use
Sans Serif

Requirements
Must have
• I'd like to see the values and org purpose depicted as one sign and as separate signs (i.e., values on one sign and org purpose on another). I need it to reflect our brand identity which I've uploaded

```html
<!DOCTYPE html>
<html lang="en">
<head>
<meta charset="utf-8">
<title>Core Values Sign</title>
<link href="https://fonts.googleapis.com/css2?family=Caladea:wght@400&display=swap" rel="stylesheet">
<style>
  :root {
    --paper: #ffffff;
    --lime: #c2d62e;
    --ink: #464a52;
    --ink-soft: #55595e;
    --white: #ffffff;
  }
  html, body {
    margin: 0;
    padding: 0;
    width: 740px;
    height: 1200px;
    overflow: hidden;
    background: var(--paper);
  }
  .sign {
    position: relative;
    width: 740px;
    height: 1200px;
    font-family: "Caladea", serif;
  }
  .panel {
    position: absolute;
    left: 28px;
    top: 18px;
    width: 682px;
    height: 1072px;
    background: var(--lime);
  }
  .title {
    position: absolute;
    left: 65px;
    margin: 0;
    font-weight: 400;
    font-size: 104px;
    line-height: 1;
    color: var(--ink);
    white-space: nowrap;
  }
  .rule {
    position: absolute;
    background: var(--white);
    height: 3px;
  }
  .rule--title { left: 65px; top: 287px; width: 364px; }
  .rule--end { left: 570px; top: 1019px; width: 121px; }
  .value-name {
    position: absolute;
    left: 63px;
    margin: 0;
    font-weight: 400;
    font-size: 66px;
    line-height: 1;
    color: var(--ink);
    white-space: nowrap;
  }
  .value-name--soft { color: var(--ink-soft); }
  .value-text {
    position: absolute;
    left: 67px;
    width: 620px;
    margin: 0;
    font-size: 34px;
    line-height: 43px;
    color: var(--white);
  }
  .brand {
    position: absolute;
    left: 0;
    width: 740px;
    top: 1118px;
    display: flex;
    justify-content: center;
    align-items: center;
    gap: 10px;
    font-size: 30px;
    line-height: 1;
    color: var(--ink);
  }
  .brand__dot {
    width: 14px;
    height: 14px;
    background: var(--lime);
  }
</style>
</head>
<body>
<main class="sign">
  <section class="panel"></section>

  <h1 class="title" style="top:57px">Core Values</h1>
  <h1 class="title" style="top:172px">Defines</h1>
  <div class="rule rule--title"></div>

  <h2 class="value-name value-name--soft" style="top:313px">Respect</h2>
  <p class="value-text" style="top:385px">We are transparent and receptive to the thoughts, opinions, and feelings to others</p>

  <h2 class="value-name" style="top:514px">Integrity</h2>
  <p class="value-text" style="top:598px">We uphold our promises</p>

  <h2 class="value-name" style="top:668px">Excellence</h2>
  <p class="value-text" style="top:750px">We continuously strive to be the best in all endeavors</p>

  <h2 class="value-name" style="top:850px">Open mindedness</h2>
  <p class="value-text" style="top:925px">We encourage creative and innovative expressions</p>

  <div class="rule rule--end"></div>

  <footer class="brand">
    <span class="brand__dot"></span>
    <span class="brand__name">Vantero</span>
  </footer>
</main>
</body>
</html>
```